New Company Business Card design

Looking for a corporate looking business card utilising my new logo design - the logo i would like embossed as one option and flat as another - simplistic but stylish - less is more - we are an import export business launching into the market - i would like a couple of options as main background - Grey or Black

```html
<!DOCTYPE html>
<html lang="en">
<head>
<meta charset="utf-8">
<title>Meridian Trade Partners – Business Card</title>
<link rel="stylesheet" href="https://fonts.googleapis.com/css2?family=Open+Sans:wght@400;600&display=swap">
<style>
  :root {
    --stage: #021a29;
    --card-white: #ffffff;
    --brand-grey: #6d6e71;
    --brand-blue: #0e6ca8;
    --text-dark: #3d3d3f;
    --text-mid: #58595b;
  }
  * { margin: 0; padding: 0; box-sizing: border-box; }
  html, body { width: 1200px; height: 1200px; overflow: hidden; background: var(--stage); }
  body { position: relative; font-family: "Open Sans", Arial, sans-serif; }

  .card {
    position: absolute;
    width: 745px;
    height: 426px;
    overflow: hidden;
    box-shadow: 0 4px 14px rgba(0, 0, 0, 0.45);
  }
  .card--front { left: 111px; top: 109px; background: var(--card-white); }
  .card--back  { left: 343px; top: 666px; background: var(--brand-grey); }

  .card__art { position: absolute; top: 0; bottom: 0; width: 250px; }
  .card--front .card__art {
    left: 0;
    background: linear-gradient(90deg, var(--brand-grey) 0%, #4f6f8c 55%, var(--brand-blue) 100%);
  }
  .card--back .card__art {
    right: 0;
    background: linear-gradient(270deg, var(--card-white) 0%, #8fb4cf 45%, var(--brand-blue) 100%);
  }

  .wordmark {
    position: absolute;
    display: flex;
    flex-direction: column;
    gap: 14px;
    font-weight: 600;
    font-size: 22px;
    letter-spacing: 0.06em;
    line-height: 1.15;
    text-transform: uppercase;
  }
  .wordmark__dot { width: 62px; height: 62px; border-radius: 50%; }
  .card--front .wordmark { right: 32px; top: 46px; align-items: flex-end; text-align: right; color: var(--brand-blue); }
  .card--front .wordmark__dot { background: var(--brand-blue); }
  .card--back .wordmark { left: 33px; top: 46px; align-items: flex-start; color: var(--card-white); }
  .card--back .wordmark__dot { background: var(--card-white); }

  .person { position: absolute; right: 33px; top: 232px; text-align: right; }
  .person__name { font-weight: 600; font-size: 31px; line-height: 1; color: var(--text-dark); }
  .person__name .initial { color: var(--brand-blue); }
  .person__role { margin-top: 8px; font-size: 21px; color: var(--text-mid); }

  .contact {
    position: absolute; right: 32px; top: 321px;
    list-style: none; text-align: right;
    font-size: 18px; line-height: 25px; color: var(--text-mid);
  }

  .address {
    position: absolute; left: 33px; top: 332px;
    font-style: normal; font-size: 21px; line-height: 29px; color: var(--card-white);
  }
</style>
</head>
<body>

  <section class="card card--front" aria-label="Business card front">
    <div class="card__art" role="img" aria-label="Decorative sweep of grey and blue bands along the left edge"></div>
    <div class="wordmark">
      <span class="wordmark__dot"></span>
      <span class="wordmark__name">Meridian Trade Partners</span>
    </div>
    <div class="person">
      <h1 class="person__name"><span class="initial">J</span>OHN <span class="initial">D</span>OE</h1>
      <p class="person__role">Director</p>
    </div>
    <ul class="contact">
      <li>+63 917 555 0142</li>
      <li>john@meridiantradepartners.com</li>
      <li>www.meridiantradepartners.com</li>
    </ul>
  </section>

  <section class="card card--back" aria-label="Business card back">
    <div class="card__art" role="img" aria-label="Decorative sweep of white and blue bands along the right edge"></div>
    <div class="wordmark">
      <span class="wordmark__dot"></span>
      <span class="wordmark__name">Meridian Trade Partners</span>
    </div>
    <address class="address">
      Dummy Street<br>
      Dummy City, Dummy Country
    </address>
  </section>

</body>
</html>
```